Stationary/Biz Card for Small Business Coaches
Bramblecrest Advisory Circle
Professional
Martin Kalbrun
President
418 Fenwick Lane
Larkmoor, NR 50294
mkalbrun@bramblecrestadvisory.example
www.bramblecrestadvisory.example
Tag line: Walking With Leaders to Achieve Growth

```html
<!DOCTYPE html>
<html lang="en">
<head>
<meta charset="utf-8">
<title>Bramblecrest Advisory Circle – Business Card</title>
<link rel="stylesheet" href="https://fonts.googleapis.com/css2?family=Cinzel:wght@600&family=Crimson+Text:wght@400;600&display=swap">
<style>
  :root {
    --page: #e6e4e1;
    --card: #ffffff;
    --navy: #1f4f9e;
    --band: #2b57a9;
    --band-dark: #234a93;
    --orange: #e2723b;
    --ink-light: #ffffff;
    --shadow: rgba(0, 0, 0, 0.22);
  }
  * { margin: 0; padding: 0; box-sizing: border-box; }
  html, body { width: 1200px; height: 1000px; overflow: hidden; }
  body {
    background: var(--page);
    position: relative;
    font-family: "Crimson Text", Georgia, serif;
  }
  .card {
    position: absolute;
    background: var(--card);
    border-radius: 22px;
    overflow: hidden;
    box-shadow: 0 10px 26px var(--shadow);
  }
  .card--front { left: 90px; top: 45px; width: 800px; height: 470px; }
  .card--back { left: 330px; top: 560px; width: 790px; height: 400px; }

  .brand {
    position: absolute;
    left: 0; right: 0;
    display: flex;
    align-items: center;
    justify-content: center;
    gap: 16px;
    white-space: nowrap;
  }
  .brand__dot {
    width: 28px; height: 28px;
    border-radius: 50%;
    background: var(--orange);
    flex: none;
  }
  .brand__name {
    font-family: "Cinzel", Georgia, serif;
    font-weight: 600;
    color: var(--navy);
    text-transform: uppercase;
    letter-spacing: 1px;
    line-height: 1;
    font-size: 32px;
  }
  .card--front .brand { top: 120px; }
  .card--back .brand { top: 180px; }

  .band {
    position: absolute;
    left: 0; right: 0;
    top: 215px; height: 185px;
    background: linear-gradient(180deg, var(--band) 0%, var(--band-dark) 100%);
  }
  .nameplate {
    position: absolute;
    left: 170px; top: 0;
    width: 400px; height: 40px;
    background: var(--orange);
    color: var(--ink-light);
    display: flex;
    align-items: center;
    padding-left: 44px;
    font-size: 21px;
    font-weight: 600;
    white-space: nowrap;
  }
  .nameplate__divider { margin: 0 12px; }
  .nameplate__title { font-weight: 400; }

  .contact {
    position: absolute;
    left: 250px; top: 60px;
    color: var(--ink-light);
    font-size: 16px;
    line-height: 1.45;
    white-space: nowrap;
  }

  .website {
    position: absolute;
    left: 0; right: 0;
    text-align: center;
    color: var(--navy);
    font-size: 17px;
    font-weight: 600;
    letter-spacing: 0.3px;
  }
  .card--front .website { top: 420px; }
  .card--back .website { top: 335px; font-size: 16px; }
</style>
</head>
<body>
  <section class="card card--front">
    <div class="brand">
      <span class="brand__dot"></span>
      <span class="brand__name">Bramblecrest Advisory Circle</span>
    </div>
    <div class="band">
      <div class="nameplate">
        <span class="nameplate__name">Martin Kalbrun</span>
        <span class="nameplate__divider">|</span>
        <span class="nameplate__title">President</span>
      </div>
      <div class="contact">
        <p>418 Fenwick Lane, Larkmoor, NR 50294</p>
        <p>P: 555-210-0148 | C: 555-210-0193</p>
        <p>E: mkalbrun@bramblecrestadvisory.example</p>
      </div>
    </div>
    <p class="website">www.bramblecrestadvisory.example</p>
  </section>

  <section class="card card--back">
    <div class="brand">
      <span class="brand__dot"></span>
      <span class="brand__name">Bramblecrest Advisory Circle</span>
    </div>
    <p class="website">www.bramblecrestadvisory.example</p>
  </section>
</body>
</html>
```